Garage Door Company seeking business card designs.
Harbor Ridge Door
Professional
Miles Tandry
Owner, Operator.
We don't want a address listed...
Miles@HarborRidgeDoor.com
www.PortalLiftExperts.com
We want to publish three numbers: Winsted - 320.555.0147 Glencoe - 320.555.0192 St. Boni - 952.555.0163 on front... Commercial and Residential On back... New Garage Door Sales and Installation. Repair and Maintenance Services. List website; www.PortalLiftExperts.com Have name, title, phone numbers, email, and website on one side. Motto's and verbiage on the other back side. Logo likely on front very prominently. Front can be full color, and back should be back letter, or the door of the logo lettering.
"If you can't get it up, we can!" Sales and Installation. Repair and Maintenance.

```html
<!DOCTYPE html>
<html lang="en">
<head>
<meta charset="utf-8">
<title>Harbor Ridge Door – Business Cards</title>
<link rel="stylesheet" href="https://fonts.googleapis.com/css2?family=Open+Sans:ital,wght@0,400;0,600;0,700;1,400&display=swap">
<style>
  :root {
    --forest: #3f4b17;
    --forest-dark: #333d12;
    --paper: #ffffff;
    --stage: #e6e6e2;
    --ink-soft: #e9ecdf;
  }
  * { margin: 0; padding: 0; box-sizing: border-box; }
  html, body { width: 1200px; height: 904px; overflow: hidden; }
  body {
    background: var(--stage);
    font-family: "Open Sans", Arial, sans-serif;
    position: relative;
  }
  .card {
    position: absolute;
    width: 560px;
    height: 320px;
    border-radius: 14px;
    overflow: hidden;
    box-shadow: 0 6px 18px rgba(0,0,0,.18);
  }

  /* Back card: motto side */
  .card-back {
    left: 90px; top: 90px;
    background: var(--forest);
    color: var(--paper);
    text-align: center;
  }
  .brand {
    display: flex; align-items: center; justify-content: center; gap: 12px;
  }
  .brand-mark {
    width: 22px; height: 22px; border-radius: 50%;
    background: currentColor;
    flex: none;
  }
  .brand-name {
    font-weight: 700; font-size: 26px; letter-spacing: 1px; text-transform: uppercase;
    white-space: nowrap;
  }
  .card-back .brand { margin-top: 72px; }
  .motto { margin-top: 26px; font-style: italic; font-size: 13px; }
  .services { margin-top: 18px; font-size: 13px; line-height: 1.5; }
  .web-rule {
    margin-top: 22px;
    display: flex; align-items: center; justify-content: center; gap: 10px;
    font-size: 13px;
  }
  .web-rule::before, .web-rule::after {
    content: ""; width: 34px; height: 1px; background: var(--paper);
  }

  /* Front card: contact side */
  .card-front {
    left: 550px; top: 494px;
    background: var(--forest);
  }
  .card-front .split { position: absolute; inset: 0; }
  .card-front .brand {
    position: absolute; left: 24px; top: 62px;
    color: var(--forest);
    justify-content: flex-start;
    gap: 10px;
  }
  .card-front .brand-name { font-size: 16px; }
  .card-front .brand-mark { width: 16px; height: 16px; }
  .sector {
    position: absolute; left: 24px; bottom: 14px;
    font-size: 12px; color: var(--paper);
  }
  .contact {
    position: absolute; left: 340px; top: 100px;
    color: var(--paper);
  }
  .contact-name { font-size: 17px; font-weight: 600; }
  .contact-title { font-size: 12px; color: var(--ink-soft); margin-bottom: 10px; }
  .contact-line {
    display: flex; align-items: center; gap: 8px;
    font-size: 12px; line-height: 20px;
    white-space: nowrap;
  }
  .icon { width: 13px; height: 13px; flex: none; }
</style>
</head>
<body>

<section class="card card-back" aria-label="Business card back">
  <div class="brand">
    <span class="brand-mark"></span>
    <span class="brand-name">Harbor Ridge Door</span>
  </div>
  <p class="motto">"If you can't get it up, we can!"</p>
  <p class="services">Sales and Installation,<br>Repair and Maintenance</p>
  <p class="web-rule">www.PortalLiftExperts.com</p>
</section>

<section class="card card-front" aria-label="Business card front">
  <svg class="split" viewBox="0 0 560 320" preserveAspectRatio="none" aria-hidden="true">
    <polygon points="0,0 400,0 0,280" fill="#ffffff"/>
  </svg>

  <div class="brand">
    <span class="brand-mark"></span>
    <span class="brand-name">Harbor Ridge Door</span>
  </div>
  <p class="sector">Commercial and Residential</p>

  <div class="contact">
    <p class="contact-name">Miles Tandry</p>
    <p class="contact-title">Owner Operator</p>
    <p class="contact-line">
      <svg class="icon" viewBox="0 0 16 16"><circle cx="8" cy="8" r="8" fill="#fff"/><path d="M5 4.5l1.6-.4.9 2-1 .8a5.5 5.5 0 0 0 2.6 2.6l.8-1 2 .9-.4 1.6c-3.6.2-6.7-2.9-6.5-6.5z" fill="#3f4b17"/></svg>
      320.555.0147 (Winsted)
    </p>
    <p class="contact-line">
      <svg class="icon" viewBox="0 0 16 16"><circle cx="8" cy="8" r="8" fill="#fff"/><path d="M5 4.5l1.6-.4.9 2-1 .8a5.5 5.5 0 0 0 2.6 2.6l.8-1 2 .9-.4 1.6c-3.6.2-6.7-2.9-6.5-6.5z" fill="#3f4b17"/></svg>
      320.555.0192 (Glencoe)
    </p>
    <p class="contact-line">
      <svg class="icon" viewBox="0 0 16 16"><circle cx="8" cy="8" r="8" fill="#fff"/><path d="M5 4.5l1.6-.4.9 2-1 .8a5.5 5.5 0 0 0 2.6 2.6l.8-1 2 .9-.4 1.6c-3.6.2-6.7-2.9-6.5-6.5z" fill="#3f4b17"/></svg>
      952.555.0163 (St. Boni)
    </p>
    <p class="contact-line">
      <svg class="icon" viewBox="0 0 16 16"><circle cx="8" cy="8" r="8" fill="#fff"/><rect x="4" y="5.5" width="8" height="5.5" fill="none" stroke="#3f4b17" stroke-width="1.1"/><path d="M4 5.5l4 3 4-3" fill="none" stroke="#3f4b17" stroke-width="1.1"/></svg>
      Miles@HarborRidgeDoor.com
    </p>
    <p class="contact-line">
      <svg class="icon" viewBox="0 0 16 16"><circle cx="8" cy="8" r="8" fill="#fff"/><circle cx="8" cy="8" r="4" fill="none" stroke="#3f4b17" stroke-width="1.1"/><path d="M4 8h8M8 4c-1.8 2.4-1.8 5.6 0 8M8 4c1.8 2.4 1.8 5.6 0 8" fill="none" stroke="#3f4b17" stroke-width="0.9"/></svg>
      www.PortalLiftExperts.com
    </p>
  </div>
</section>

</body>
</html>
```